Defense contractor needs a roll-up for an exhibition

The booth we have booked has only a size of 3m².
So this will be the centerpiece of the whole booth.
We need a roll-up that attracts visitors and at the same time it should contain already designed graphics. These graphics are giving visitors an overview of our system. So it is necessary to have them exposed in a height that the booth personal can conveniently point with its fingers at them.
For information about our company and product visit:
https://www.brightlanternoptics.com/
For designing you should use Adobe Illustrator and the templates provided in the zip file, to guarantee a perfect print.
I have supplied my business card that you can copy the logo. As the company logo will be already at the booth nearby the top of the roll-up, you should not place it there. It can be in the middle or at the bottom.
I have uploaded a picture of the booth. The roll up will be placed at the left of the screen and has a size of 80cm x 200cm

Defense

Defense

Serif

Colors
0054AA
0677BA
7BADD7
CADEEF
E8F1F8

• you must use the Adobe Illustrator template to have a good printing result
• company logo on the upper side of the roll-up

```html
<!DOCTYPE html>
<html lang="en">
<head>
<meta charset="utf-8">
<title>Bright Lantern Optics – Roll-up</title>
<link rel="stylesheet" href="https://fonts.googleapis.com/css2?family=Bebas+Neue&family=Open+Sans:wght@400;700&display=swap">
<style>
  :root {
    --blue-deep: #163f8f;
    --blue: #1f56ad;
    --blue-light: #2e6cc4;
    --panel: #e8ebf6;
    --ink: #1c2f5e;
    --rule: #9aa3bb;
    --black: #1d1d22;
    --white: #ffffff;
    --stage: #d4d6da;
  }
  * { box-sizing: border-box; margin: 0; padding: 0; }
  html, body { width: 1200px; height: 900px; overflow: hidden; }
  body { background: var(--stage); font-family: "Open Sans", sans-serif; }

  .rollup {
    position: absolute; left: 420px; top: 10px;
    width: 360px; height: 880px;
    background: var(--panel);
    overflow: hidden;
    box-shadow: 0 6px 20px rgba(0,0,0,.18);
  }
  .rollup-shapes { position: absolute; inset: 0; }

  .headline {
    position: absolute; top: 26px; left: 0; width: 100%;
    text-align: center; color: var(--white);
    font-family: "Bebas Neue", sans-serif; font-weight: 400;
    font-size: 26px; line-height: 27px; letter-spacing: .2px;
  }

  .art { position: absolute; border-radius: 4px; }
  .art-field {
    left: 20px; top: 112px; width: 320px; height: 198px;
    background: linear-gradient(160deg, #dde0ec, #c3c9da 65%, #a8b7de);
  }
  .art-room {
    left: 26px; top: 452px; width: 316px; height: 162px;
    background: linear-gradient(170deg, #dcd8dd, #bcc2d4 60%, #a4b3dc);
  }

  .intro-band {
    position: absolute; left: 0; top: 323px; width: 100%; height: 121px;
    background: linear-gradient(90deg, var(--blue-deep), var(--blue) 55%, var(--blue-light));
    color: var(--white); text-align: center; padding: 25px 18px 0;
  }
  .brand-name {
    font-family: "Open Sans", sans-serif; font-weight: 700;
    font-size: 15px; line-height: 18px; letter-spacing: .3px; text-transform: uppercase;
  }
  .brand-name::after {
    content: ""; display: inline-block; width: 8px; height: 8px;
    background: var(--white); margin-left: 7px; vertical-align: 1px;
  }
  .intro-text {
    margin-top: 13px; text-align: justify;
    font-size: 7.5px; line-height: 10.6px;
  }

  .features {
    position: absolute; left: 24px; top: 620px; width: 319px;
    list-style: none;
    display: grid; grid-template-columns: repeat(4, 1fr);
  }
  .feature {
    height: 62px; text-align: center; padding-top: 2px;
    border-right: 1px solid var(--rule);
    line-height: 0;
  }
  .feature:nth-child(4n) { border-right: none; }
  .feature:nth-child(-n+4) { border-bottom: 1px solid var(--rule); }
  .feature:nth-child(n+5) { padding-top: 8px; }
  .feature svg { width: 28px; height: 28px; display: block; margin: 0 auto 5px; }
  .feature-label {
    display: block;
    font-size: 6.6px; font-weight: 700; line-height: 8.6px;
    color: var(--ink); text-transform: uppercase;
  }

  .contact { position: absolute; left: 25px; top: 768px; color: var(--white); }
  .contact-title {
    font-family: "Bebas Neue", sans-serif; font-weight: 400;
    font-size: 19px; line-height: 20px;
  }
  .contact-line {
    display: flex; align-items: center; gap: 6px;
    font-size: 10px; line-height: 12px; font-weight: 700; margin-top: 6px;
  }
  .contact-line svg { width: 12px; height: 12px; flex: none; }
</style>
</head>
<body>
<main class="rollup">
  <svg class="rollup-shapes" viewBox="0 0 360 880" preserveAspectRatio="none" aria-hidden="true">
    <defs>
      <linearGradient id="blueSweep" x1="0" y1="0" x2="1" y2="0">
        <stop offset="0" stop-color="#163f8f"/>
        <stop offset=".6" stop-color="#1f56ad"/>
        <stop offset="1" stop-color="#2e6cc4"/>
      </linearGradient>
    </defs>
    <polygon points="0,0 360,0 360,76 0,132" fill="url(#blueSweep)"/>
    <polygon points="0,132 360,76 360,81 0,138" fill="#ffffff"/>
    <polygon points="240,101 360,82 360,126" fill="#1d1d22"/>
    <polygon points="0,741 360,827 360,880 0,880" fill="url(#blueSweep)"/>
    <polygon points="235,793 360,757 360,827" fill="#1d1d22"/>
  </svg>

  <h1 class="headline">Advanced Combat Training Systems<br>for Realistic Combat Simulation</h1>

  <div class="art art-field" role="img" aria-label="Isometric illustration of two tanks, three target stands and an open instructor truck with screens and soldiers"></div>

  <section class="intro-band">
    <h2 class="brand-name">Bright Lantern Optics</h2>
    <p class="intro-text">LARTIS (Lantern Range Tracking And Instrumentation System) allows for a modern approach to duel simulation, firing range training, armored vehicle driving training, and simulation debriefing through an integrated system of sensors, optics, and controls that give soldiers and instructors real-time, real-world vision and data.</p>
  </section>

  <div class="art art-room" role="img" aria-label="Isometric illustration of a debriefing room with desks, seated trainees and two wall screens showing a tank and a terrain map"></div>

  <ul class="features">
    <li class="feature">
      <svg viewBox="0 0 28 28" fill="none" stroke="#1c2f5e" stroke-width="1.6"><rect x="9" y="8" width="10" height="18" rx="2"/><circle cx="14" cy="14" r="2.2"/><path d="M11.5 20h5M11.5 23h5M10 5a6 6 0 0 1 8 0M11.8 6.8a3 3 0 0 1 4.4 0"/></svg>
      <span class="feature-label">Remote-control<br>functions</span>
    </li>
    <li class="feature">
      <svg viewBox="0 0 28 28" fill="none" stroke="#1c2f5e" stroke-width="1.6"><path d="M4 6h20v4H4z"/><path d="M7 10a7 7 0 0 0 14 0"/><circle cx="14" cy="13" r="3"/><path d="M14 20v5M10 25h8"/></svg>
      <span class="feature-label">16 camera systems<br>per vehicle</span>
    </li>
    <li class="feature">
      <svg viewBox="0 0 28 28" fill="none" stroke="#1c2f5e" stroke-width="1.6"><rect x="3" y="8" width="22" height="16" rx="3"/><path d="M10 8l2-3h4l2 3"/><circle cx="14" cy="16" r="5"/><circle cx="14" cy="16" r="2.2"/></svg>
      <span class="feature-label">Optics<br>camera</span>
    </li>
    <li class="feature">
      <svg viewBox="0 0 28 28" fill="none" stroke="#1c2f5e" stroke-width="1.6"><rect x="6" y="3" width="16" height="22" rx="1.5"/><path d="M9 8h7M9 12h7M9 16h7M9 20h7"/><circle cx="19" cy="12" r=".8"/><circle cx="19" cy="16" r=".8"/></svg>
      <span class="feature-label">Vehicle<br>data</span>
    </li>
    <li class="feature">
      <svg viewBox="0 0 28 28" fill="none" stroke="#1c2f5e" stroke-width="2"><circle cx="12" cy="11" r="6.5"/><path d="M17 16l7 7"/></svg>
      <span class="feature-label">Full instructor<br>overview</span>
    </li>
    <li class="feature">
      <svg viewBox="0 0 28 28" fill="none" stroke="#1c2f5e" stroke-width="1.6"><path d="M16 4a2 2 0 0 1 4 0v13a4 4 0 1 1-4 0z"/><path d="M18 11v8"/><path d="M11 9a5 5 0 0 0 0 10z" fill="#1c2f5e"/><path d="M5 14H3M6 8.5 4.5 7M6 19.5 4.5 21"/></svg>
      <span class="feature-label">Air-conditioned<br>instructor</span>
    </li>
    <li class="feature">
      <svg viewBox="0 0 28 28" fill="none" stroke="#1c2f5e" stroke-width="1.6"><path d="M6 14a8 8 0 0 1 16 0"/><rect x="4" y="13" width="3" height="6" rx="1"/><rect x="21" y="13" width="3" height="6" rx="1"/><path d="M10 14v3M12 12v7M14 10v11M16 12v7M18 14v3"/></svg>
      <span class="feature-label">Full data<br>recording</span>
    </li>
    <li class="feature">
      <svg viewBox="0 0 28 28" fill="none" stroke="#1c2f5e" stroke-width="1.6"><path d="M2 24l10-16 4 6 3-3 7 13z"/><path d="M14 16v6M11.4 17.5l5.2 3M11.4 20.5l5.2-3"/></svg>
      <span class="feature-label">All-weather &amp;<br>all-terrain</span>
    </li>
  </ul>

  <footer class="contact">
    <h3 class="contact-title">Contact us</h3>
    <p class="contact-line">
      <svg viewBox="0 0 12 12"><rect width="12" height="12" rx="2" fill="#fff"/><path d="M3.2 2.6l1.4-.3.8 1.8-.9.7a5 5 0 0 0 2.3 2.3l.7-.9 1.8.8-.3 1.4C6 8.8 3 6 3.2 2.6z" fill="#1f56ad"/></svg>
      +49 170 555 0142
    </p>
    <p class="contact-line">
      <svg viewBox="0 0 12 12"><rect width="12" height="12" rx="2" fill="#fff"/><g fill="none" stroke="#1f56ad" stroke-width=".8"><circle cx="6" cy="6" r="3.5"/><ellipse cx="6" cy="6" rx="1.5" ry="3.5"/><path d="M2.5 6h7"/></g></svg>
      www.brightlanternoptics.com
    </p>
  </footer>
</main>
</body>
</html>
```